Tall Harbor Business Card

We are a Video Production and Video Equipment Rental company specialising in the supply of state of the art Video Technology and Services for the Live Entertainment, Television and Corporate Business Theatre markets. (in Sydney, Australia) www.tallharbor-media.example

Industry/Entity Type

Business

Contact Information for Business Card

name, position, email, website, address, logo
Example attached of the information we need - doesn't necessarily have to look the same

Font styles to use
Other font styles liked:
• Tall Harbor logo font is GOTHAM

Colors
ea1f27

Requirements
Nice to have
• either matt black or shiny black cards -
raised logo

```html
<!DOCTYPE html>
<html lang="en">
<head>
<meta charset="utf-8">
<title>Tall Harbor Business Card</title>
<link rel="stylesheet" href="https://fonts.googleapis.com/css2?family=Cinzel:wght@700&family=Spectral:wght@400;600&display=swap">
<style>
  :root {
    --page: #ffffff;
    --card-black: #030303;
    --card-white: #ffffff;
    --ink: #111111;
    --brand-red: #ea1f27;
    --soft-grey: #d8d8d8;
    --rule-grey: #4a4a4a;
  }
  * { margin: 0; padding: 0; box-sizing: border-box; }
  html, body { width: 1200px; height: 1000px; overflow: hidden; background: var(--page); }
  .canvas { position: relative; width: 1200px; height: 1000px; }

  .card {
    position: absolute;
    top: 355px;
    width: 460px;
    height: 290px;
    box-shadow: 0 3px 10px rgba(0,0,0,0.35);
  }

  /* Front face */
  .card-front { left: 120px; background: var(--card-black); }
  .front-rule {
    position: absolute; left: 70px; top: 62px; width: 215px; height: 1px; background: var(--rule-grey);
  }
  .wordmark {
    position: absolute; left: 70px; top: 84px;
    display: flex; align-items: center; gap: 12px;
  }
  .wordmark-square { width: 14px; height: 14px; background: var(--brand-red); }
  .wordmark-name {
    font-family: "Spectral", serif; font-weight: 600;
    font-size: 28px; letter-spacing: 1px; text-transform: uppercase;
    color: #ffffff;
  }
  .services {
    position: absolute; left: 108px; top: 162px; list-style: none;
    font-family: "Spectral", serif; font-size: 17px; line-height: 19px; color: var(--soft-grey);
  }
  .services li::before { content: "|| "; letter-spacing: -2px; margin-right: 4px; color: var(--soft-grey); }

  /* Back face */
  .card-back { left: 620px; background: var(--card-white); }
  .frame { position: absolute; left: 18px; top: 20px; width: 424px; height: 250px; }
  .person {
    position: absolute; left: 0; width: 100%; text-align: center;
    font-family: "Cinzel", serif; font-weight: 700;
  }
  .person-name {
    top: 58px; font-size: 31px; line-height: 38px; color: var(--ink);
    text-shadow: 2px 2px 2px rgba(0,0,0,0.3);
  }
  .person-role {
    top: 100px; font-size: 18px; line-height: 22px; color: var(--brand-red); letter-spacing: 0.5px;
    text-shadow: 1px 1px 1px rgba(0,0,0,0.25);
  }
  .address {
    position: absolute; left: 0; top: 148px; width: 100%; text-align: center;
    font-family: "Spectral", serif; font-size: 16px; line-height: 17px; color: var(--ink);
  }
  .web, .email {
    position: absolute; left: 0; width: 100%; text-align: center;
    font-family: "Spectral", serif; font-size: 15px; line-height: 18px;
  }
  .web { top: 212px; color: var(--brand-red); }
  .email { top: 243px; color: var(--ink); }
</style>
</head>
<body>
<main class="canvas">
  <section class="card card-front" aria-label="Card front">
    <div class="front-rule"></div>
    <div class="wordmark">
      <span class="wordmark-square"></span>
      <span class="wordmark-name">Tall Harbor</span>
    </div>
    <ul class="services">
      <li>Video Solutions</li>
      <li>Led Screens</li>
      <li>Camera Systems</li>
      <li>Projection</li>
    </ul>
  </section>

  <section class="card card-back" aria-label="Card back">
    <svg class="frame" viewBox="0 0 424 250" aria-hidden="true">
      <g fill="none" stroke-width="2.5">
        <polyline points="2,20 2,2 422,2 422,20" stroke="#111111"/>
        <polyline points="10,20 10,10 414,10 414,20" stroke="#ea1f27"/>
        <polyline points="414,202 414,218 10,218 10,202" stroke="#ea1f27"/>
        <polyline points="422,228 422,248 2,248 2,228" stroke="#111111"/>
      </g>
    </svg>
    <div class="person person-name">Dan Carvello</div>
    <div class="person person-role">Managing Director</div>
    <p class="address">18 Wharf Lane<br>Marrick NSW 2099<br>Australia</p>
    <p class="web">www.tallharbor-media.example</p>
    <p class="email">Email: dan@tallharbor-media.example</p>
  </section>
</main>
</body>
</html>
```